Storm Restoration Contractor needs a professional business card design

Looking for a professional business card design. Not looking for your cheapo MS Word standard ones that are readily available. Dont want it to be cookie cutter look like ones readily available online. We just recently changed our logo and want to freshen up all our documents. Our company handles restoring a property back to a pre-loss condition after a storm damages it. For example, wind, hail, flood, fire losses.

Target Market(s)

Property Owners, Homeowners, Property Owners, Commercial Property Owners, Property Management Companies, Hail and Wind Damaged Properties

Industry/Entity Type

Construction Company

Contact Information for Business Card

Brightline Facades
847-555-0193
847-555-0147 fax
www.brightlinefacades.example
info@brightlinefacades.example

Requirements
Must have
• Clean, Professional, fresh look
• Storm Restoration, Roofing, Siding, Windows
Nice to have
• If there is a way to incorporate storms that may be cool.

```html
<!DOCTYPE html>
<html lang="en">
<head>
<meta charset="utf-8">
<title>Brightline Facades – Business Card</title>
<link href="https://fonts.googleapis.com/css2?family=Cabin:wght@500;600&display=swap" rel="stylesheet">
<style>
  :root {
    --backdrop: #87958f;
    --ink: #0a0a0a;
    --brand-blue: #2a84f5;
    --white: #ffffff;
  }
  html, body {
    margin: 0;
    padding: 0;
    width: 980px;
    height: 1200px;
    overflow: hidden;
    background: var(--backdrop);
    font-family: "Cabin", Arial, sans-serif;
  }
  .card {
    position: absolute;
    left: 120px;
    width: 718px;
    height: 408px;
    overflow: hidden;
  }
  .card--front { top: 132px; }
  .card--back { top: 711px; width: 712px; height: 410px; background: var(--brand-blue); }
  .card svg.card-art {
    position: absolute;
    inset: 0;
    width: 100%;
    height: 100%;
  }
  .wordmark {
    position: absolute;
    left: 0;
    right: 0;
    text-align: center;
    color: var(--brand-blue);
    font-weight: 600;
    letter-spacing: 2px;
    text-transform: uppercase;
    margin: 0;
  }
  .card--front .wordmark { top: 224px; font-size: 24px; }
  .card--back .wordmark { top: 112px; font-size: 20px; }
  .company-name {
    position: absolute;
    left: 54px;
    top: 268px;
    margin: 0;
    color: var(--white);
    font-size: 29px;
    font-weight: 600;
  }
  .divider {
    position: absolute;
    left: 343px;
    top: 222px;
    width: 4px;
    height: 163px;
    background: var(--white);
  }
  .contact-list {
    position: absolute;
    left: 376px;
    top: 244px;
    margin: 0;
    padding: 0;
    list-style: none;
    color: var(--white);
  }
  .contact-list li {
    display: flex;
    align-items: center;
    height: 32px;
  }
  .contact-list li.contact--small { height: 30px; font-size: 17.5px; }
  .contact-list li.contact--large { font-size: 22px; }
  .contact-list svg {
    width: 24px;
    height: 24px;
    margin-right: 34px;
    flex: none;
  }
</style>
</head>
<body>

<section class="card card--front">
  <svg class="card-art" viewBox="0 0 718 408" preserveAspectRatio="none">
    <defs>
      <linearGradient id="front-top" x1="0" y1="0" x2="1" y2="0.3">
        <stop offset="0" stop-color="#2f6cf0"/>
        <stop offset="0.25" stop-color="#5fd0f0"/>
        <stop offset="0.38" stop-color="#66f01a"/>
        <stop offset="0.55" stop-color="#3aa8f5"/>
        <stop offset="0.72" stop-color="#e03ad8"/>
        <stop offset="1" stop-color="#1f2ee0"/>
      </linearGradient>
      <linearGradient id="front-bottom" x1="0" y1="0" x2="1" y2="0">
        <stop offset="0" stop-color="#c81a3a"/>
        <stop offset="0.25" stop-color="#ff4a1a"/>
        <stop offset="0.5" stop-color="#f0a818"/>
        <stop offset="0.68" stop-color="#e8e040"/>
        <stop offset="0.82" stop-color="#7ef5f0"/>
        <stop offset="1" stop-color="#3aa8f0"/>
      </linearGradient>
    </defs>
    <rect class="pattern pattern--top" role="img" aria-label="Colourful low-poly triangle pattern in blues, greens and magentas" x="0" y="0" width="718" height="215" fill="url(#front-top)"/>
    <rect class="pattern pattern--bottom" role="img" aria-label="Colourful low-poly triangle pattern in reds, oranges, yellows and cyan" x="0" y="305" width="718" height="103" fill="url(#front-bottom)"/>
    <path class="band" d="M0 211 H163 V140 L357 106 L558 140 V211 H718 V309 H0 Z" fill="var(--ink)"/>
  </svg>
  <p class="wordmark">Brightline Facades</p>
</section>

<section class="card card--back">
  <svg class="card-art" viewBox="0 0 712 410" preserveAspectRatio="none">
    <defs>
      <linearGradient id="back-top" x1="0" y1="0" x2="1" y2="0">
        <stop offset="0" stop-color="#3a6ef0"/>
        <stop offset="0.2" stop-color="#f07a20"/>
        <stop offset="0.32" stop-color="#70e830"/>
        <stop offset="0.5" stop-color="#f0c030"/>
        <stop offset="0.65" stop-color="#f0f040"/>
        <stop offset="0.8" stop-color="#e83ad0"/>
        <stop offset="1" stop-color="#2a2ee0"/>
      </linearGradient>
    </defs>
    <rect class="pattern" role="img" aria-label="Colourful low-poly triangle pattern strip" x="0" y="0" width="712" height="95" fill="url(#back-top)"/>
    <path class="band" d="M0 93 H237 L356 52 L473 93 H712 V170 H473 L356 210 L237 170 H0 Z" fill="var(--ink)"/>
  </svg>
  <p class="wordmark">Brightline Facades</p>

  <h1 class="company-name">Brightline Facades</h1>
  <div class="divider"></div>

  <ul class="contact-list">
    <li class="contact--large">
      <svg viewBox="0 0 24 24" aria-label="Phone"><path d="M6.6 3.5 9 6.4c.4.5.4 1.2-.1 1.6L7.6 9.2c.9 2.3 2.8 4.3 5.2 5.2l1.2-1.3c.4-.5 1.1-.5 1.6-.1l2.9 2.4c.5.4.5 1.1.1 1.6l-1.5 1.7c-.6.6-1.5.9-2.4.6C9.2 17.6 6.4 14.8 4.7 9.3c-.3-.9 0-1.8.6-2.4Z" fill="var(--white)"/></svg>
      847-555-0193
    </li>
    <li class="contact--large">
      <svg viewBox="0 0 24 24" aria-label="Fax"><g fill="none" stroke="var(--white)" stroke-width="1.6"><rect x="3" y="9" width="18" height="10" rx="1"/><path d="M7 9V3h10v6M7 16h10M8 12h3"/></g></svg>
      847-555-0147
    </li>
    <li class="contact--small">
      <svg viewBox="0 0 24 24" aria-label="Email"><g fill="none" stroke="var(--white)" stroke-width="1.6"><rect x="3" y="6" width="18" height="13" rx="1"/><path d="M3 7l9 7 9-7"/></g></svg>
      info@brightlinefacades.example
    </li>
    <li class="contact--small">
      <svg viewBox="0 0 24 24" aria-label="Website"><g fill="none" stroke="var(--white)" stroke-width="1.5"><circle cx="12" cy="12" r="9"/><ellipse cx="12" cy="12" rx="4" ry="9"/><path d="M3 12h18M5 7h14M5 17h14"/></g></svg>
      www.brightlinefacades.example
    </li>
  </ul>
</section>

</body>
</html>
```